Prepared Meal Company Needs Menu Design

We are a pre-prepared meal delivery company called Krumb Kettlery.

We have a menu in excel but needs to be designed to look good and appealing to customers. The menu should be clean, easy to ready, and show:Title (Pupusa)Tags (V, V+, GF - Use a cool vegan logo for the V+ and logo for vegetarian V symbol)Price (12.99)DescriptionBrand colors are orange white and green. Design is clean, crisp and can incorporate natural elements like leaf shaped symbols, etc. Screenshots from our website attached for inspiration.

Target Market(s)

Broad demographics

Industry/Entity Type

Restaurant

Font styles to use
Sans Serif

Requirements
Must have
• The menu design should be commensurate with the website under development
• https://krumbkettlery.dishlyst.com
Nice to have
• Should have appropriate graphics
Should not have
• Modifiers do not need to be shown (these are shown in the excel only).

```html
<!DOCTYPE html>
<html lang="en">
<head>
<meta charset="utf-8">
<title>Krumb Kettlery Menu</title>
<link href="https://fonts.googleapis.com/css2?family=Oswald:wght@400;500&family=Dancing+Script:wght@500;700&display=swap" rel="stylesheet">
<style>
  :root {
    --backdrop: #333333;
    --paper: #fbfbfa;
    --orange: #f26a21;
    --green: #2f7d2f;
    --ink: #1e1e1e;
    --leaf-light: #c7e0a8;
    --leaf-mid: #8fc27a;
  }
  * { margin: 0; padding: 0; box-sizing: border-box; }
  html, body { width: 1200px; height: 1200px; overflow: hidden; background: var(--backdrop); }
  .menu-sheet {
    position: absolute; left: 195px; top: 25px; width: 812px; height: 1150px;
    background: var(--paper); overflow: hidden;
  }
  .leaf-art { position: absolute; border-radius: 50%; opacity: .55; }
  .leaf-art.top { left: 200px; top: -40px; width: 380px; height: 330px;
    background: radial-gradient(circle at 50% 40%, var(--leaf-mid), var(--leaf-light) 60%, transparent 72%); }
  .leaf-art.left-mid { left: -60px; top: 300px; width: 200px; height: 200px;
    background: radial-gradient(circle, var(--leaf-mid), transparent 70%); }
  .leaf-art.right-mid { left: 690px; top: 200px; width: 200px; height: 220px;
    background: radial-gradient(circle, var(--leaf-mid), transparent 70%); }
  .leaf-art.right-sand { left: 640px; top: 430px; width: 260px; height: 300px;
    background: radial-gradient(circle, var(--leaf-light), transparent 70%); }
  .leaf-art.bottom-left { left: -40px; top: 720px; width: 560px; height: 520px;
    background: radial-gradient(circle at 55% 55%, var(--leaf-mid), var(--leaf-light) 55%, transparent 72%); }
  .leaf-art.bottom-right { left: 620px; top: 880px; width: 300px; height: 360px;
    background: radial-gradient(circle, var(--leaf-mid), var(--leaf-light) 50%, transparent 72%); }

  .ribbon { position: absolute; width: 367px; height: 56px; }
  .ribbon svg { position: absolute; inset: 0; }
  .ribbon h2 {
    position: relative; text-align: center; line-height: 56px;
    font-family: "Oswald", sans-serif; font-weight: 400; font-size: 22px;
    color: #fff; letter-spacing: .3px;
  }
  .section { position: absolute; width: 378px; font-family: "Dancing Script", cursive; --lh: 21px; }
  .item-name {
    display: flex; align-items: baseline; color: var(--green);
    font-weight: 700; font-size: 15.5px; line-height: var(--lh); height: var(--lh);
  }
  .item-name .leader { flex: 1; border-bottom: 1.5px dotted #777; margin: 0 4px; transform: translateY(-4px); }
  .item-name .price { font-size: 17px; line-height: var(--lh); }
  .item-name.wrap { display: block; }
  .desc { color: var(--ink); font-weight: 500; font-size: 15px; line-height: var(--lh); }
</style>
</head>
<body>
<main class="menu-sheet">
  <div class="leaf-art top" role="img" aria-label="Illustrated leafy greens and asparagus"></div>
  <div class="leaf-art left-mid" role="img" aria-label="Illustrated leaf"></div>
  <div class="leaf-art right-mid" role="img" aria-label="Illustrated asparagus and leaves"></div>
  <div class="leaf-art right-sand" role="img" aria-label="Illustrated lettuce leaves"></div>
  <div class="leaf-art bottom-left" role="img" aria-label="Illustrated lettuce leaves and asparagus"></div>
  <div class="leaf-art bottom-right" role="img" aria-label="Illustrated lettuce leaves and asparagus"></div>

  <div class="ribbon" style="left:18px;top:48px">
    <svg viewBox="0 0 367 56" preserveAspectRatio="none"><polygon points="0,0 367,0 350,28 367,56 0,56 17,28" fill="var(--orange)"/></svg>
    <h2>ENTREES</h2>
  </div>
  <section class="section" style="left:12px;top:115px;--lh:21.2px">
    <div class="item-name">Grilled Pacific Ocean Perch &amp; Mango Tacos (GF)<span class="leader"></span><span class="price">9.49$</span></div>
    <p class="desc">Salsa Roja, Cilantro-Lime Yogurt, Arugula &amp; Inca<br>Corn with Fresh Mango on 2 Handmade Corn Tortillas.</p>
    <div class="item-name">Butternut &amp; Chayote Squash Succotash (V+, GF)<span class="leader"></span><span class="price">9.49$</span></div>
    <p class="desc">Heirloom Ayocote Beans, Sugar Snap Peas, Roasted<br>Bell Pepper, Onion &amp; Garlic, Vegan Butter, Rosemary,<br>Epazote &amp; Oregano</p>
    <div class="item-name">Aztec Gold Chili (V+, GF)<span class="leader"></span><span class="price">9.99$</span></div>
    <p class="desc">Rancho Verde Hominy, Coconut Milk, Pasilla, Guajillo<br>&amp; Chile Negro, Cane Sugar, Oregano &amp; Epazote, Inca Corn<br>Crumble, Tropical Acai Hot Sauce</p>
    <div class="item-name wrap">Pacific Ocean Perch Filet with Heirloom</div>
    <div class="item-name">Ayocote Beans (GF, Dairy Free)<span class="leader"></span><span class="price">14.99$</span></div>
    <p class="desc">Asparagus &amp; Grilled Meyer Lemon, Coastal, Epazote, Cilantro</p>
    <div class="item-name">Scottish Salmon (GF)<span class="leader"></span><span class="price">15.99$</span></div>
    <p class="desc">Lemon &amp; Dill Yogurt, Roasted Potatoes, Caramelized<br>Tomato &amp; Asparagus, Sea Salt</p>
    <div class="item-name">Oaxacan Chicken (GF)<span class="leader"></span><span class="price">13.99$</span></div>
    <p class="desc">Whole Herb Marinade, Heirloom Ayocote Beans,<br>Salsa Roja, Guacamole, Cilantro-Lime Yogurt with<br>Handmade Tortillas</p>
    <div class="item-name">Sous Vide Bison Shortribs (GF, Dairy Free)<span class="leader"></span><span class="price">15.99$</span></div>
    <p class="desc">African Sorghum, Torn Mint, Braised Fennel,<br>Orange Supremes, Sugar Snap Peas &amp; Roasted Carrots</p>
  </section>

  <div class="ribbon" style="left:18px;top:638px">
    <svg viewBox="0 0 367 56" preserveAspectRatio="none"><polygon points="0,0 367,0 350,28 367,56 0,56 17,28" fill="var(--orange)"/></svg>
    <h2>DRINKS</h2>
  </div>
  <section class="section" style="left:12px;top:704px;--lh:20.9px">
    <div class="item-name">The Clover Juice<span class="leader"></span><span class="price">7.49$</span></div>
    <p class="desc">Tall Orchard Brand. Kale, Cucumber, Celery, Spinach,<br>Pear, Cilantro, Mint, Lime</p>
    <div class="item-name">Go Big<span class="leader"></span><span class="price">7.49$</span></div>
    <p class="desc">Tall Orchard Brand. Beet, Kale, Carrot, Apple, Wheat<br>Grass, Lemon, Ginger</p>
    <div class="item-name">Gingersnap<span class="leader"></span><span class="price">7.49$</span></div>
    <p class="desc">Tall Orchard Brand. Fuji Apple, Green Apple, Lemon, Ginger</p>
    <div class="item-name">The Quench<span class="leader"></span><span class="price">7.49$</span></div>
    <p class="desc">Tall Orchard Brand. Watermelon, Jicama, Strawberry,<br>Mint, Lime, Watermelon Rind</p>
    <div class="item-name">Sunrise<span class="leader"></span><span class="price">7.49$</span></div>
    <p class="desc">Tall Orchard Brand. Carrot, Orange, Coconut Water,<br>Turmeric, Lemon, Ginger</p>
    <div class="item-name">Hawaiian Hazelnut Cold Brew<span class="leader"></span><span class="price">3.00$</span></div>
    <p class="desc">Housemade Hawaiian Hazelnut Cold-Brewed Coffee</p>
    <div class="item-name">Hawaiian Hazelnut Cold Brew<span class="leader"></span><span class="price">5.00$</span></div>
    <p class="desc">Hemp-Derived CBD &amp; Extra Virgin Coconut Oil<br>blended with our Hazelnut Cold-Brewed Coffee</p>
  </section>

  <div class="ribbon" style="left:425px;top:50px">
    <svg viewBox="0 0 367 56" preserveAspectRatio="none"><polygon points="0,0 367,0 350,28 367,56 0,56 17,28" fill="var(--orange)"/></svg>
    <h2>DESSERT</h2>
  </div>
  <section class="section" style="left:419px;top:119px;--lh:21.7px">
    <div class="item-name">Goji-Macaccino Brownies (V+, GF)<span class="leader"></span><span class="price">5.99$</span></div>
    <p class="desc">Goji Berries, Coconut, Vegan Dark Chocolate Chips<br>&amp; Maca Powder</p>
    <div class="item-name">Cranberry-Pistachio Protein Cookie Bar (V+, GF)<span class="leader"></span><span class="price">4.99$</span></div>
    <p class="desc">Almond &amp; Meyer Lemon, Moringa, Maca, Cane Sugar,<br>Ceylon Cinnamon</p>
    <div class="item-name">Seasonal Berries &amp; Coconut Yogurt (V+, GF)<span class="leader"></span><span class="price">6.49$</span></div>
    <p class="desc">Lavender-Banana Crumble, Seasonal Berries</p>
    <div class="item-name">Apricot &amp; Pear Tartlettes (3) (V+, GF)<span class="leader"></span><span class="price">3.99$</span></div>
    <p class="desc">Apricot-Pear Compote, Vanilla &amp; Almond filled<br>Gluten-Free &amp; Vegan Tart Crusts</p>
    <div class="item-name">Coconut-Raspberry Tartlettes (3) (V+, GF)<span class="leader"></span><span class="price">3.99$</span></div>
    <p class="desc">Coconut Whipped Cream &amp; Raspberry filled Gluten<br>Free &amp; Vegan Tart Crusts</p>
  </section>

  <div class="ribbon" style="left:425px;top:446px">
    <svg viewBox="0 0 367 56" preserveAspectRatio="none"><polygon points="0,0 367,0 350,28 367,56 0,56 17,28" fill="var(--orange)"/></svg>
    <h2>SANDWICHES &amp; FLATBREADS</h2>
  </div>
  <section class="section" style="left:419px;top:513px;--lh:20.65px">
    <div class="item-name">Salmon Burger<span class="leader"></span><span class="price">14.99$</span></div>
    <p class="desc">Lemon-Dill Yogurt, Baby Spinach, Black Pepper<br>&amp; Braised Cherry Tomatoes on Harvest 4:9 Sprouted<br>Whole Wheat Toast</p>
    <div class="item-name wrap">Moroccan Red Lentil Burger</div>
    <div class="item-name">(V) [ V+ No Chamomile Yogurt]<span class="leader"></span><span class="price">12.99$</span></div>
    <p class="desc">Moroccan Spiced Grain &amp; Vegetable Patty, Baby<br>Spinach, Cherry Tomatoes and Saffron-Chamomile<br>Yogurt on Harvest 4:9 Sprouted Whole Wheat Toast</p>
    <div class="item-name">Local Buratta &amp; Fig Flatbread (V, GF)<span class="leader"></span><span class="price">10.99$</span></div>
    <p class="desc">California Figs, Vellara Buratta, Raw Honey, Toasted<br>Almond, Sumac &amp; Sugar Snap Peas on Handmade<br>Gluten-Free Flatbread</p>
    <div class="item-name">Chicken Caprese Flatbread (GF)<span class="leader"></span><span class="price">12.99$</span></div>
    <p class="desc">Marla's Grilled Chicken, Roasted Cherry Tomato, Basil,<br>Goat Cheese &amp; Saba on Handmade Gluten Free Flatbread</p>
    <div class="item-name">California Sunshine Flatbread (V, GF)<span class="leader"></span><span class="price">10.99$</span></div>
    <p class="desc">Roasted Cherry Tomato, Asparagus &amp; Arugula,<br>Chevre, Crisped Inca Corn, Poached Egg on Handmade<br>Gluten-Free Flatbread</p>
    <div class="item-name wrap">Bison Shortrib &amp; Creamy Mushroom</div>
    <div class="item-name">Flatbread (GF)<span class="leader"></span><span class="price">13.99$</span></div>
    <p class="desc">Goat Cheese, Sugar Snap Peas, Radish, Roasted Garlic<br>&amp; Mushroom Sauce on Handmade Gluten-Free Flatbread</p>
    <div class="item-name">Marinated Squash Flatbread (V, GF)<span class="leader"></span><span class="price">9.49$</span></div>
    <p class="desc">Chayote Escabeche, Avocado, Pepitas, Ancho Oil, Cilantro<br>&amp; Inca Corn Crumble on Handmade Gluten-Free Flatbread</p>
  </section>
</main>
</body>
</html>
```